Dental Medical History Form - Content provided

Design a medical history form for a dental practice. Content is provided so all that is needed is the formatting to make it look great and easy to read.

"Patient Information" to include all information contained in top portion of the "Patient Medical History Form" docx file.

"Medical History" should follow the formatting and content of the "Exact Medical History" file as this is what the entry fields look like in our practice software and so we would like it to match.

1st page - Patient info, allergies, medications, antibiotics, joint replacement, pregnancy.

2nd page - Do you have, or have you had, any of the following? . . . . . . .

Target Market(s)

All ages but must be clear enough for elderly to read. Use as much space as possible to keep font size bigger yet keep to two pages

Industry/Entity Type

Dental

Font styles to use
Sans Serif

Requirements
Must have
• All content provided
• Our logo at the top (file provided)
• Century Gothic Font
• Limit to two pages

```html
<!DOCTYPE html>
<html lang="en">
<head>
<meta charset="utf-8">
<title>Harbourline Dental – Confidential Medical History</title>
<link rel="stylesheet" href="https://fonts.googleapis.com/css2?family=Arimo:wght@400;700&display=swap">
<style>
:root{
  --bg:#e4e2df;
  --paper:#ffffff;
  --ink:#1d1d1d;
  --band-dark:#4a4b4d;
  --band-light:#d9d9d9;
  --rule:#6f6f6f;
}
*{box-sizing:border-box;margin:0;padding:0}
html,body{width:1200px;height:900px;overflow:hidden;background:var(--bg)}
body{font-family:"Arimo",Arial,sans-serif;color:var(--ink);position:relative}
.page{position:absolute;top:57px;width:560px;height:786px;background:var(--paper);box-shadow:0 3px 10px rgba(0,0,0,.25)}
.page-one{left:30px}
.page-two{left:612px}
.abs{position:absolute}
.brand-name{left:29px;top:40px;font-size:17px;font-weight:700;color:var(--ink);line-height:1;white-space:nowrap}
.title-band{left:262px;top:38px;width:298px;height:22px;background:var(--band-dark);clip-path:polygon(0 0,100% 0,100% 100%,14px 100%);color:#fff;font-weight:700;font-size:14.5px;line-height:22px;padding-left:22px;letter-spacing:.3px}
.field{position:absolute;display:flex;align-items:flex-end;font-size:10.5px;white-space:nowrap}
.field .line{flex:1;border-bottom:1px solid var(--rule);margin-left:4px;height:1px;position:relative}
.field .line em{position:absolute;top:3px;font-style:normal;font-size:5.5px}
.col-l{left:29px;width:241px}
.col-r{left:289px;width:243px}
.heading{position:absolute;font-weight:700;font-size:11px}
.text{position:absolute;font-size:10.5px;line-height:13px;white-space:nowrap}
.box{display:inline-block;width:7px;height:7px;border:1px solid var(--ink);margin:0 4px 0 0;vertical-align:0}
.opts{position:absolute;font-size:10.5px;white-space:nowrap;display:flex;gap:11px}
.rule{position:absolute;left:29px;width:502px;border-bottom:1px solid var(--rule)}
.footer{position:absolute;left:0;top:744px;width:560px;height:16px;background:var(--band-light)}
.footer .addr{position:absolute;left:0;top:0;height:16px;width:392px;background:var(--band-dark);clip-path:polygon(0 0,100% 0,calc(100% - 10px) 100%,0 100%);color:#fff;font-size:11px;line-height:16px;padding-left:24px}
.footer .phone{position:absolute;left:410px;top:0;line-height:16px;font-weight:700;font-size:13px;color:var(--ink);padding-left:18px}
.footer svg{position:absolute;top:3px}
.q-title{left:29px;top:27px;font-weight:700;font-size:12.5px}
.group{position:absolute;width:242px;font-size:9.6px}
.group h3{font-size:10px;font-weight:700;height:13.3px;line-height:13.3px}
.group ul{list-style:none}
.group li{height:13.3px;line-height:13.3px;display:flex;justify-content:space-between;white-space:nowrap}
.group li .yn{display:flex;gap:6px;width:61px}
.group li .box{width:6px;height:6px;margin-right:3px}
.group .small{font-size:8.2px}
.thanks{position:absolute;left:0;width:560px;text-align:center;font-size:7.6px;line-height:11px}
.thanks i{display:block}
</style>
</head>
<body>

<section class="page page-one">
  <div class="abs brand-name">Harbourline Dental</div>
  <div class="abs title-band">CONFIDENTIAL MEDICAL HISTORY</div>

  <div class="field col-l" style="top:96px">Name :<span class="line"><em style="left:8px">First</em><em style="left:86px">Middle</em><em style="left:162px">Last</em></span></div>
  <div class="field col-l" style="top:122px">Address :<span class="line"></span></div>
  <div class="field col-l" style="top:149px">DOB :<span class="line"></span></div>
  <div class="field col-l" style="top:175px">Email Address :<span class="line"></span></div>
  <div class="field col-l" style="top:202px">Phone Number(s) :<span class="line"><em style="left:22px">Mobile</em><em style="left:76px">Work</em><em style="left:122px">Home</em></span></div>

  <div class="heading" style="left:29px;top:255px">Emergency Contact Person</div>
  <div class="field col-l" style="top:281px">Name :<span class="line"></span></div>
  <div class="field col-l" style="top:307px">Relationship :<span class="line"></span></div>
  <div class="field col-l" style="top:333px">Phone Number :<span class="line"></span></div>

  <div class="heading" style="left:289px;top:95px">General Practitioner</div>
  <div class="field col-r" style="top:122px">Name :<span class="line"></span></div>
  <div class="field col-r" style="top:149px">Practice Name :<span class="line"></span></div>
  <div class="field col-r" style="top:175px">Phone Number :<span class="line"></span></div>
  <div class="text" style="left:289px;top:201px">Do you have a health fund with<br>dental cover?</div>
  <div class="opts" style="left:452px;top:214px"><span><span class="box"></span>Yes</span><span><span class="box"></span>No</span></div>
  <div class="text" style="left:289px;top:240px">If so, what is the name of</div>
  <div class="field col-r" style="top:253px">the fund?<span class="line"></span></div>
  <div class="field col-r" style="top:280px">Fund Number?<span class="line"></span></div>
  <div class="text" style="left:289px;top:306px">Priority Number of card :&nbsp; 0 &nbsp;1 &nbsp;2 &nbsp;3 &nbsp;4 &nbsp;5</div>

  <div class="heading" style="left:29px;top:360px">Please indicate if you are allergic to any of the following ☑ ?</div>
  <div class="opts" style="left:29px;top:386px;gap:13px"><span><span class="box"></span>Aspirin</span><span><span class="box"></span>Codeine</span><span><span class="box"></span>Penicillin</span><span><span class="box"></span>Sulfites</span><span><span class="box"></span>Latex</span><span><span class="box"></span>Local Anaesthetic</span><span><span class="box"></span>Lactose</span><span><span class="box"></span>Nickel</span></div>
  <div class="field" style="left:29px;width:502px;top:412px"><span><span class="box"></span>Other :</span><span class="line"></span></div>

  <div class="heading" style="left:29px;top:441px">Are you currently taking, or have ever taken, any of the following medication ☑ ?</div>
  <div class="opts" style="left:29px;top:465px;gap:13px"><span><span class="box"></span>Asthma inhaler</span><span><span class="box"></span>Anti-epileptics</span><span><span class="box"></span>Anti-depressants</span><span><span class="box"></span>Blood Pressure</span><span><span class="box"></span>Blood Thinners</span></div>
  <div class="opts" style="left:29px;top:486px;gap:12px"><span><span class="box"></span>Bisphosphonates</span><span><span class="box"></span>Chemotherapy</span><span><span class="box"></span>Insulin</span><span><span class="box"></span>Immunosuppressants</span><span><span class="box"></span>Steroids</span></div>
  <div class="field" style="left:29px;width:502px;top:512px"><span><span class="box"></span>Oral Contraceptive &nbsp;&nbsp;<span class="box"></span>Other :</span><span class="line"></span></div>

  <div class="heading" style="left:29px;top:547px">Please specify medication name, does, and frequency where possible.</div>
  <div class="rule" style="top:581px"></div>
  <div class="rule" style="top:608px"></div>
  <div class="rule" style="top:635px"></div>

  <div class="text" style="left:40px;top:653px">Do you require antibiotic cover?&nbsp;&nbsp;&nbsp; <span class="box"></span>Yes&nbsp;&nbsp; <span class="box"></span>No</div>
  <div class="text" style="left:40px;top:680px">Have you had a joint replacement ?&nbsp; <span class="box"></span>Yes&nbsp;&nbsp; <span class="box"></span>No</div>
  <div class="heading" style="left:40px;top:705px">Women:</div>
  <div class="text" style="left:40px;top:721px">Are you Pregnant?&nbsp;&nbsp;&nbsp; <span class="box"></span>Yes&nbsp; <span class="box"></span>No&nbsp; <span class="box"></span>Possible&nbsp;&nbsp;&nbsp;&nbsp;&nbsp;&nbsp;&nbsp; Breast Feeding?&nbsp; <span class="box"></span>Yes&nbsp;&nbsp; <span class="box"></span>No</div>

  <div class="footer">
    <div class="addr">Harbourline Dental, 3.05/120 Coastal Road, Bayview NSW. 2260</div>
    <svg style="left:9px" width="8" height="10" viewBox="0 0 8 10"><path d="M4 0a4 4 0 0 1 4 4c0 3-4 6-4 6S0 7 0 4a4 4 0 0 1 4-4z" fill="#fff"/><circle cx="4" cy="4" r="1.5" fill="#4a4b4d"/></svg>
    <svg style="left:410px" width="11" height="11" viewBox="0 0 12 12"><circle cx="6" cy="6" r="5.3" fill="none" stroke="#1d1d1d"/><path d="M4 3.2l1 1.3-.6.8c.4.8 1 1.4 1.8 1.8l.8-.6 1.3 1-.6 1C5.6 8.3 3.7 6.4 3.1 3.8z" fill="#1d1d1d"/></svg>
    <div class="phone">(02) 45 210 390</div>
  </div>
</section>

<section class="page page-two">
  <div class="abs q-title">Do you have, or have you had, any of the following?</div>

  <div class="group" style="left:29px;top:47px"><h3>Dental</h3><ul>
    <li>Acid Reflux<span class="yn"><span><span class="box"></span>Yes</span><span><span class="box"></span>No</span></span></li>
    <li>Bad Breath/Taste<span class="yn"><span><span class="box"></span>Yes</span><span><span class="box"></span>No</span></span></li>
    <li>Bleeding/Swollen/Sore Gums<span class="yn"><span><span class="box"></span>Yes</span><span><span class="box"></span>No</span></span></li>
    <li>Blisters/Ulcers in Mouth<span class="yn"><span><span class="box"></span>Yes</span><span><span class="box"></span>No</span></span></li>
    <li>Broken tooth/filling<span class="yn"><span><span class="box"></span>Yes</span><span><span class="box"></span>No</span></span></li>
    <li>Burning tongue<span class="yn"><span><span class="box"></span>Yes</span><span><span class="box"></span>No</span></span></li>
    <li>Dry mouth<span class="yn"><span><span class="box"></span>Yes</span><span><span class="box"></span>No</span></span></li>
    <li>Food collection between teeth<span class="yn"><span><span class="box"></span>Yes</span><span><span class="box"></span>No</span></span></li>
    <li>Grinding/Clenching teeth (day/night)<span class="yn"><span><span class="box"></span>Yes</span><span><span class="box"></span>No</span></span></li>
    <li>loose teeth<span class="yn"><span><span class="box"></span>Yes</span><span><span class="box"></span>No</span></span></li>
    <li>Crooked teeth<span class="yn"><span><span class="box"></span>Yes</span><span><span class="box"></span>No</span></span></li>
    <li>Discoloured teeth<span class="yn"><span><span class="box"></span>Yes</span><span><span class="box"></span>No</span></span></li>
    <li>Sensitivity to Hot/Cold<span class="yn"><span><span class="box"></span>Yes</span><span><span class="box"></span>No</span></span></li>
    <li>Tooth pain when chewing<span class="yn"><span><span class="box"></span>Yes</span><span><span class="box"></span>No</span></span></li>
    <li>Jaw Pain/Fracture<span class="yn"><span><span class="box"></span>Yes</span><span><span class="box"></span>No</span></span></li>
    <li>Orthodontic treatment/history<span class="yn"><span><span class="box"></span>Yes</span><span><span class="box"></span>No</span></span></li>
    <li>Oral Cancer<span class="yn"><span><span class="box"></span>Yes</span><span><span class="box"></span>No</span></span></li>
  </ul></div>

  <div class="group" style="left:29px;top:297px"><h3>Diet/Lifestyle</h3><ul>
    <li><span class="small">Drink more than one glass alchohol per day</span><span class="yn"><span><span class="box"></span>Yes</span><span><span class="box"></span>No</span></span></li>
    <li>Smoking<span class="yn"><span><span class="box"></span>Yes</span><span><span class="box"></span>No</span></span></li>
    <li>Carbonated drinks<span class="yn"><span><span class="box"></span>Yes</span><span><span class="box"></span>No</span></span></li>
    <li>Sugary foods<span class="yn"><span><span class="box"></span>Yes</span><span><span class="box"></span>No</span></span></li>
  </ul></div>

  <div class="group" style="left:29px;top:377px"><h3>Blood</h3><ul>
    <li>Anaemia<span class="yn"><span><span class="box"></span>Yes</span><span><span class="box"></span>No</span></span></li>
    <li>Blood clots<span class="yn"><span><span class="box"></span>Yes</span><span><span class="box"></span>No</span></span></li>
    <li>Leukemia<span class="yn"><span><span class="box"></span>Yes</span><span><span class="box"></span>No</span></span></li>
    <li>Low platelets<span class="yn"><span><span class="box"></span>Yes</span><span><span class="box"></span>No</span></span></li>
    <li>Lymphoma<span class="yn"><span><span class="box"></span>Yes</span><span><span class="box"></span>No</span></span></li>
    <li>Haemophelia<span class="yn"><span><span class="box"></span>Yes</span><span><span class="box"></span>No</span></span></li>
  </ul></div>

  <div class="group" style="left:29px;top:483px"><h3>Chest</h3><ul>
    <li>Bronchitis<span class="yn"><span><span class="box"></span>Yes</span><span><span class="box"></span>No</span></span></li>
    <li>Cystic Fibrosis<span class="yn"><span><span class="box"></span>Yes</span><span><span class="box"></span>No</span></span></li>
    <li>Emphysema<span class="yn"><span><span class="box"></span>Yes</span><span><span class="box"></span>No</span></span></li>
    <li>Pneumonia<span class="yn"><span><span class="box"></span>Yes</span><span><span class="box"></span>No</span></span></li>
  </ul></div>

  <div class="group" style="left:29px;top:563px"><h3>Infectious Disease</h3><ul>
    <li>Creutzfeldt-Jakob Disease<span class="yn"><span><span class="box"></span>Yes</span><span><span class="box"></span>No</span></span></li>
    <li>Hepatitis A,B,C,D<span class="yn"><span><span class="box"></span>Yes</span><span><span class="box"></span>No</span></span></li>
    <li>HIV/AIDS<span class="yn"><span><span class="box"></span>Yes</span><span><span class="box"></span>No</span></span></li>
    <li>Influenza<span class="yn"><span><span class="box"></span>Yes</span><span><span class="box"></span>No</span></span></li>
    <li>Shingles<span class="yn"><span><span class="box"></span>Yes</span><span><span class="box"></span>No</span></span></li>
    <li>Tuberculosis<span class="yn"><span><span class="box"></span>Yes</span><span><span class="box"></span>No</span></span></li>
  </ul></div>

  <div class="group" style="left:293px;top:47px"><h3>Heart</h3><ul>
    <li>Angina<span class="yn"><span><span class="box"></span>Yes</span><span><span class="box"></span>No</span></span></li>
    <li>Atrial fibrillation<span class="yn"><span><span class="box"></span>Yes</span><span><span class="box"></span>No</span></span></li>
    <li>Blood Pressure (high/low)<span class="yn"><span><span class="box"></span>Yes</span><span><span class="box"></span>No</span></span></li>
    <li>Congenital heart disease<span class="yn"><span><span class="box"></span>Yes</span><span><span class="box"></span>No</span></span></li>
    <li>Heart attack<span class="yn"><span><span class="box"></span>Yes</span><span><span class="box"></span>No</span></span></li>
    <li>Heart murmur<span class="yn"><span><span class="box"></span>Yes</span><span><span class="box"></span>No</span></span></li>
    <li>Heart surgery<span class="yn"><span><span class="box"></span>Yes</span><span><span class="box"></span>No</span></span></li>
    <li>Heart valve replacement<span class="yn"><span><span class="box"></span>Yes</span><span><span class="box"></span>No</span></span></li>
    <li>Infective endocarditis<span class="yn"><span><span class="box"></span>Yes</span><span><span class="box"></span>No</span></span></li>
    <li>Rheumatic heart disease<span class="yn"><span><span class="box"></span>Yes</span><span><span class="box"></span>No</span></span></li>
    <li>Pacemaker<span class="yn"><span><span class="box"></span>Yes</span><span><span class="box"></span>No</span></span></li>
    <li>Stent<span class="yn"><span><span class="box"></span>Yes</span><span><span class="box"></span>No</span></span></li>
  </ul></div>

  <div class="group" style="left:293px;top:228px"><h3>Other</h3><ul>
    <li>Anxiety/PTSD<span class="yn"><span><span class="box"></span>Yes</span><span><span class="box"></span>No</span></span></li>
    <li>Arthritis<span class="yn"><span><span class="box"></span>Yes</span><span><span class="box"></span>No</span></span></li>
    <li>Alzheimer's<span class="yn"><span><span class="box"></span>Yes</span><span><span class="box"></span>No</span></span></li>
    <li>Asthma<span class="yn"><span><span class="box"></span>Yes</span><span><span class="box"></span>No</span></span></li>
    <li>Anaphylaxis<span class="yn"><span><span class="box"></span>Yes</span><span><span class="box"></span>No</span></span></li>
    <li>Auto-immune disease<span class="yn"><span><span class="box"></span>Yes</span><span><span class="box"></span>No</span></span></li>
    <li>Coeliac<span class="yn"><span><span class="box"></span>Yes</span><span><span class="box"></span>No</span></span></li>
    <li>Depression<span class="yn"><span><span class="box"></span>Yes</span><span><span class="box"></span>No</span></span></li>
    <li>Diabetes<span class="yn"><span><span class="box"></span>Yes</span><span><span class="box"></span>No</span></span></li>
    <li>Epilepsy<span class="yn"><span><span class="box"></span>Yes</span><span><span class="box"></span>No</span></span></li>
    <li>Kidney disease<span class="yn"><span><span class="box"></span>Yes</span><span><span class="box"></span>No</span></span></li>
    <li>Liver disease<span class="yn"><span><span class="box"></span>Yes</span><span><span class="box"></span>No</span></span></li>
    <li>Osteoporosis<span class="yn"><span><span class="box"></span>Yes</span><span><span class="box"></span>No</span></span></li>
    <li>Parkinson's<span class="yn"><span><span class="box"></span>Yes</span><span><span class="box"></span>No</span></span></li>
    <li>Radiation to head/neck<span class="yn"><span><span class="box"></span>Yes</span><span><span class="box"></span>No</span></span></li>
    <li>Schizophrenia<span class="yn"><span><span class="box"></span>Yes</span><span><span class="box"></span>No</span></span></li>
    <li>Snoring<span class="yn"><span><span class="box"></span>Yes</span><span><span class="box"></span>No</span></span></li>
    <li>Sleep apnea<span class="yn"><span><span class="box"></span>Yes</span><span><span class="box"></span>No</span></span></li>
    <li>Stroke<span class="yn"><span><span class="box"></span>Yes</span><span><span class="box"></span>No</span></span></li>
  </ul></div>

  <div class="field" style="left:293px;width:240px;top:508px;font-size:9.6px">Other :<span class="line" style="margin-left:10px"></span></div>
  <div class="rule" style="left:325px;width:208px;top:533px"></div>
  <div class="rule" style="left:325px;width:208px;top:553px"></div>
  <div class="field" style="left:293px;width:240px;top:616px;font-size:9.6px">Signature :<span class="line"></span></div>
  <div class="field" style="left:293px;width:240px;top:643px;font-size:9.6px">Date :<span class="line"></span></div>

  <div class="thanks" style="top:713px">Thank you for the time to complete your medical history form.<i>Oral health is linked overall health and this comprehensive questionnaire will help us to provide you with optimal ans safe care.</i></div>

  <div class="footer">
    <div class="addr">Harbourline Dental, 3.05/120 Coastal Road, Bayview NSW. 2260</div>
    <svg style="left:9px" width="8" height="10" viewBox="0 0 8 10"><path d="M4 0a4 4 0 0 1 4 4c0 3-4 6-4 6S0 7 0 4a4 4 0 0 1 4-4z" fill="#fff"/><circle cx="4" cy="4" r="1.5" fill="#4a4b4d"/></svg>
    <svg style="left:410px" width="11" height="11" viewBox="0 0 12 12"><circle cx="6" cy="6" r="5.3" fill="none" stroke="#1d1d1d"/><path d="M4 3.2l1 1.3-.6.8c.4.8 1 1.4 1.8 1.8l.8-.6 1.3 1-.6 1C5.6 8.3 3.7 6.4 3.1 3.8z" fill="#1d1d1d"/></svg>
    <div class="phone">(02) 45 210 390</div>
  </div>
</section>

</body>
</html>
```